電子書籍の表紙デザインをお願い致します。

本の内容、
冴えない20代のOLでした。そんな私でしたが約7年前に、
「たった一度きりのこの人生。もっと自分らしく、もっと輝かせたい。」
と強く熱望した瞬間があり、私は知識・人脈・実績・経験・貯金などビジネスに関してプラスになるような持ち合わせが一切ないゼロの状態で、【私らしい生き方と働き方】を一心に求めて「起業」を目指しはじめました。
今では独立を果たし、当時は未知の世界でしかなかった独立起業の道も今年で7年目に突入しました。得意な分野は、ビジネスコンサルティング、ビジネスプロデュース、コミュニティ運営、Webマーケティング、Webライティング、アフィリエイト、プロモーション、マインドコーチング、オウンドメディア構築など。写真や動画の編集・加工などクリエイティブなことも割と好きです。

私の仕事における共通点はどのビジネスでもパソコン1台とネット環境があれば場所を問わずどこでも仕事ができることです。そのライフスタイルを「スカイハーベスター」と名付け、よく国内外問わず、大好きな旅をしながら仕事をしています。

しかし、この 「起業」という働き方に出会う前の私は、好きなことをしながら仕事ができる、そんなワークスタイルがあるだなんて夢にも思っていませんでした。
そんなの理想のまた理想・・・そんなかんじで。しかしそれ以上に私が伝えたいのは、「自分でビジネスをして価値提供をする」という中で自分の思考や価値観、ライフスタイルまでも大きく変化したということなのです。そして今は毎日に充実感があり、やりがいを感じながら仕事も楽しくしています。

そして現在は、自らの経験と海外で得た感動をもとにPC1台で好きな時に・好きな場所で・好きな人と、「自分らしく、グローバルに生きていく」そんなスタイルを日々全力で、熱狂してご提供しています。

優しい雰囲気の安心できるような女性らしいカラーでお願い致します。

使って頂きたい画像と本文を添付致します。
表紙はこの4枚の画像を使って優しいイメージで、パステルカラー、薄い色を使っていただけると嬉しいです。

タイトルは
きみの毎日は花になる!扉をそっと叩いて
心ほどける日々を選び取るための小さな習慣集
でお願い致します。

はじめに、私の起業ストーリーを少しお話しさせてください。私はもともと自分に自信がまったく持てなくて、そのくせ社会不適合で、ただただ路頭に迷う、冴えない20代のOLでした。そんな私でしたが約7年前に、

日にちを19日まで延長させていただきました。
20日まで延長致しました。宜しくお願い致します。
いま、
最終段階で決定に向けて進めております。
21日で締め切らせていただきます。最後までよろしくお願いいたします。

お洒落な大人女子のイメージややんわりとしたパステルカラーの色合いがとても美しい作品だと感じました。タイトルや入れたい文字をしっかりと目立たせていただきました。自分の思い描くイメージをカタチにしてくださったなと感謝の想いでいっぱいでございます。

この度、ご提案してくださったデザイナーの皆様、最後まで吟味させて頂き、選ぶのにとても迷いました。それほど、素晴らしい作品ばかりでした。沢山のご提案を本当に有難うございました。今回はご縁を頂けなかった皆様とも、今後も定期的にコンペをさせていただく予定ですので、どうぞよろしくお願いします。

```html
<!DOCTYPE html>
<html lang="ja">
<head>
<meta charset="utf-8">
<title>心ほどける日々を選び取るための小さな習慣集</title>
<link rel="stylesheet" href="https://fonts.googleapis.com/css2?family=M+PLUS+Rounded+1c:wght@500;800&family=Klee+One:wght@600&family=Great+Vibes&display=swap">
<style>
  :root {
    --pink: #e8579a;
    --pink-soft: #f59ac3;
    --pink-tag: #f07fb1;
    --ink: #4a4650;
    --white: #ffffff;
    --sky: #cfe7f4;
    --pool: #8fd0e6;
    --blush: #f8e1ec;
    --sand: #efe3d6;
  }
  html, body { margin: 0; padding: 0; overflow: hidden; }
  body { width: 750px; height: 1200px; background: var(--white); }
  .cover {
    position: relative; width: 750px; height: 1200px; overflow: hidden;
    font-family: "M PLUS Rounded 1c", sans-serif; color: var(--ink);
  }
  .scene-photo {
    position: absolute; inset: 0;
    background:
      radial-gradient(ellipse at 60% 70%, var(--pool) 0%, rgba(143,208,230,0) 35%),
      linear-gradient(180deg, #fbf6fb 0%, var(--blush) 30%, var(--sky) 55%, var(--sand) 80%, #f3e6ef 100%);
  }
  .veil {
    position: absolute; left: 0; right: 0; top: 0; height: 560px;
    background: linear-gradient(180deg, rgba(255,255,255,.85) 0%, rgba(255,255,255,.6) 70%, rgba(255,255,255,0) 100%);
  }
  .lead-bubble {
    position: absolute; left: 137px; top: 20px; width: 476px; height: 62px;
    background: var(--white); border-radius: 31px;
    box-shadow: 0 2px 10px rgba(232,87,154,.18);
    display: flex; align-items: center; justify-content: center;
    font-family: "Klee One", cursive; font-size: 38px; color: var(--ink); white-space: nowrap;
  }
  .lead-sub {
    position: absolute; left: 0; right: 0; top: 102px; text-align: center;
    font-size: 44px; font-weight: 500; color: var(--ink); white-space: nowrap;
    text-shadow: 0 0 8px var(--white);
  }
  .title-badge {
    position: absolute; left: 62px; top: 168px; width: 220px; height: 90px;
    background: var(--white); border: 4px solid var(--pink-soft); border-radius: 45px;
    display: flex; align-items: center; justify-content: center;
    font-family: "Klee One", cursive; font-size: 42px; color: var(--pink); white-space: nowrap;
    transform: rotate(-6deg);
  }
  .title-line {
    position: absolute; font-weight: 800; color: var(--pink); white-space: nowrap;
    text-shadow: 0 0 6px var(--white), 0 0 12px var(--white), 0 3px 0 var(--white);
  }
  .title-line.one { left: 300px; top: 150px; font-size: 96px; }
  .title-line.two { left: 40px; top: 268px; font-size: 90px; letter-spacing: -2px; }
  .title-line.three { left: 0; right: 0; top: 388px; text-align: center; font-size: 74px; color: var(--ink); }
  .snapshot {
    position: absolute; margin: 0; background: var(--white); padding: 10px 10px 22px;
    box-shadow: 0 4px 12px rgba(0,0,0,.15);
  }
  .snapshot .photo { width: 100%; height: 100%; }
  .snapshot.group { left: 50px; top: 510px; width: 240px; height: 190px; transform: rotate(-4deg); }
  .snapshot.group .photo { background: linear-gradient(135deg, #d9b8a6, #b99a8e 60%, #e6d3c4); }
  .snapshot.garden { left: 42px; top: 712px; width: 180px; height: 168px; transform: rotate(3deg); }
  .snapshot.garden .photo { background: linear-gradient(160deg, #b9d6a8, #8fb88a 55%, #e5d7c4); }
  .snapshot.flowers { left: 232px; top: 735px; width: 160px; height: 240px; transform: rotate(-3deg); }
  .snapshot.flowers .photo { background: linear-gradient(180deg, #9cc39a, #e9a7c3 50%, #88b382); }
  .author {
    position: absolute; left: 30px; top: 1000px; width: 260px; text-align: center;
    color: var(--white); text-shadow: 0 1px 6px rgba(120,90,110,.55); white-space: nowrap;
  }
  .author .brand { font-family: "Great Vibes", cursive; font-size: 44px; line-height: 1.1; }
  .author .name { font-size: 26px; letter-spacing: 4px; font-weight: 500; line-height: 1.3; }
  .style-tag {
    position: absolute; white-space: nowrap;
    font-family: "Klee One", cursive; font-size: 24px; line-height: 1; color: var(--white);
    background: var(--pink-tag); border-radius: 8px; padding: 8px 14px;
    transform: rotate(-6deg);
  }
  .style-tag.pc { left: 398px; top: 915px; }
  .style-tag.time { left: 432px; top: 962px; }
  .style-tag.place { left: 502px; top: 1008px; }
  .style-tag.people { left: 596px; top: 1054px; }
  .closing-line {
    position: absolute; left: 0; right: 0; top: 1118px; height: 70px;
    background: linear-gradient(90deg, rgba(255,255,255,.85), rgba(255,240,247,.92), rgba(255,255,255,.85));
    display: flex; align-items: center; justify-content: center; white-space: nowrap;
    font-size: 40px; font-weight: 800; color: var(--pink);
    text-shadow: 0 0 4px var(--white), 0 0 8px var(--white);
  }
  .sparkle { position: absolute; }
</style>
</head>
<body>
<main class="cover">
  <div class="scene-photo" role="img" aria-label="プールサイドのテラスでノートパソコンを開いて仕事をする女性の写真"></div>
  <div class="veil"></div>

  <svg class="sparkle" style="left:30px;top:40px" width="60" height="60" viewBox="0 0 60 60" aria-hidden="true">
    <path d="M30 4 L34 26 L56 30 L34 34 L30 56 L26 34 L4 30 L26 26 Z" fill="none" stroke="#c9a6d8" stroke-width="2"/>
  </svg>
  <svg class="sparkle" style="left:660px;top:470px" width="50" height="50" viewBox="0 0 60 60" aria-hidden="true">
    <path d="M30 4 L34 26 L56 30 L34 34 L30 56 L26 34 L4 30 L26 26 Z" fill="none" stroke="#f59ac3" stroke-width="2"/>
  </svg>

  <div class="lead-bubble">きみの毎日は花になる！</div>
  <div class="lead-sub">扉をそっと叩いて</div>

  <div class="title-badge">心ほどける</div>
  <div class="title-line one">日々を</div>
  <div class="title-line two">選び取るための</div>
  <div class="title-line three">小さな習慣集</div>

  <figure class="snapshot group"><div class="photo" role="img" aria-label="大勢の子どもたちと並んだ集合写真"></div></figure>
  <figure class="snapshot garden"><div class="photo" role="img" aria-label="緑の庭で過ごす女性の写真"></div></figure>
  <figure class="snapshot flowers"><div class="photo" role="img" aria-label="花のアーチの下に立つ子どもの写真"></div></figure>

  <div class="style-tag pc">PC1台で</div>
  <div class="style-tag time">好きな時に</div>
  <div class="style-tag place">好きな場所で</div>
  <div class="style-tag people">好きな人と</div>

  <div class="author">
    <div class="brand">Sky Harvester</div>
    <div class="name">MIOKA</div>
  </div>

  <div class="closing-line">自分らしく、グローバルに生きていく</div>
</main>
</body>
</html>
```